QLB Insurance Services Business Card
Slogan - Quiet Lanterns Burn
Creative Brief
Use specific fonts
Feel free to use the same font as used in my logo OR whatever looks good
Simple
Marisol (Greta) Dovik
Broker
20387 Marlowpine Dr. Tustin, CA 92740
greta@qlbinsurance.example
www.qblinsurance.example
0K47382
*Commercial Liability *Commercial Property *Business Owner Policy *Excess/Umbrella Liability *Worker's Compensation *Professional Liability *Commercial/Business Auto *Homeowner/Auto Insurance *Flood/Earthquake Insurance and more *Specializing import/export and manufacture company

```html
<!DOCTYPE html>
<html lang="en">
<head>
<meta charset="utf-8">
<title>QLB Insurance Services – Business Card</title>
<link rel="stylesheet" href="https://fonts.googleapis.com/css2?family=Arimo:ital,wght@0,400;0,700;1,700&display=swap">
<style>
  :root {
    --stage: #2b2b2b;
    --card: #ffffff;
    --blue: #2a9fe0;
    --blue-light: #8fd3f7;
    --blue-deep: #1574b8;
    --ink: #1a1a1a;
    --muted: #555555;
    --icon: #d9363e;
  }
  * { box-sizing: border-box; margin: 0; padding: 0; }
  html, body { width: 1200px; height: 761px; overflow: hidden; }
  body {
    background: var(--stage);
    font-family: "Arimo", Arial, sans-serif;
    color: var(--ink);
    position: relative;
  }
  .card {
    position: absolute;
    width: 518px;
    height: 307px;
    background: var(--card);
    overflow: hidden;
    box-shadow: 0 4px 10px rgba(0,0,0,.45);
  }
  .card--front   { left: 77px;  top: 48px; }
  .card--back    { left: 629px; top: 48px; }
  .card--front-b { left: 77px;  top: 396px; }
  .card--back-b  { left: 629px; top: 396px; }
  .card__art { position: absolute; inset: 0; width: 100%; height: 100%; }

  .brand {
    position: absolute;
    left: 0; right: 0;
    text-align: center;
  }
  .brand__mark {
    font-weight: 700;
    font-size: 30px;
    letter-spacing: 2px;
    color: var(--ink);
    line-height: 1;
  }
  .brand__name {
    margin-top: 8px;
    font-weight: 700;
    font-size: 25px;
    letter-spacing: .3px;
    line-height: 1;
  }
  .brand__slogan {
    margin: 4px auto 0;
    width: 250px;
    font-size: 15px;
    font-weight: 700;
    color: var(--blue-deep);
    background: linear-gradient(to bottom, #ffffff 0%, #d6effc 55%, var(--blue-light) 100%);
    border-bottom: 3px solid var(--blue);
    line-height: 18px;
  }
  .person {
    position: absolute; left: 0; right: 0; text-align: center;
    font-size: 15px;
  }
  .person__name { font-weight: 700; font-style: italic; }
  .person__role { color: var(--muted); padding-left: 6px; margin-left: 4px; border-left: 1px solid var(--muted); }
  .license { font-size: 10px; color: var(--muted); margin-top: 4px; }

  .contact {
    position: absolute;
    font-size: 10px;
    color: var(--muted);
    line-height: 15px;
  }
  .contact__row { display: flex; align-items: center; gap: 5px; white-space: nowrap; }
  .icon { width: 9px; height: 9px; flex: none; }

  .header-name {
    position: absolute; left: 0; right: 0; top: 16px; text-align: center; color: #fff;
  }
  .header-name__name { font-size: 24px; font-weight: 700; font-style: italic; }
  .header-name__role { font-size: 14px; margin-top: 4px; }

  .web {
    position: absolute; left: 0; right: 0; bottom: 30px; text-align: center;
    font-size: 10px; color: var(--muted);
  }
</style>
</head>
<body>

<svg width="0" height="0" style="position:absolute">
  <defs>
    <linearGradient id="band" x1="0" y1="0" x2="0" y2="1">
      <stop offset="0" stop-color="#1574b8"/>
      <stop offset="1" stop-color="#4cc0f2"/>
    </linearGradient>
    <symbol id="phone" viewBox="0 0 10 10">
      <circle cx="5" cy="5" r="5" fill="#d9363e"/>
      <path d="M3 2.6 4.1 2.3 4.6 3.8 4 4.3Q4.5 5.4 5.7 6L6.2 5.4 7.7 5.9 7.4 7Q4 7.3 3 2.6Z" fill="#fff"/>
    </symbol>
    <symbol id="mail" viewBox="0 0 10 10">
      <circle cx="5" cy="5" r="5" fill="#d9363e"/>
      <rect x="2.5" y="3.3" width="5" height="3.4" fill="#fff"/>
      <path d="M2.5 3.3 5 5.2 7.5 3.3" fill="none" stroke="#d9363e" stroke-width=".6"/>
    </symbol>
  </defs>
</svg>

<!-- Front: name below brand -->
<section class="card card--front">
  <svg class="card__art" viewBox="0 0 518 307" preserveAspectRatio="none" aria-hidden="true">
    <path d="M0 0H518V20C380 62 170 10 0 40Z" fill="url(#band)"/>
    <path d="M0 58C140 18 330 44 518 22V30C330 56 150 28 0 62Z" fill="#111"/>
    <rect x="0" y="299" width="518" height="4" fill="var(--blue)"/>
  </svg>
  <div class="brand" style="top:72px">
    <div class="brand__mark">QLB</div>
    <div class="brand__name">QLB Insurance Services</div>
    <div class="brand__slogan">Quiet Lanterns Burn</div>
  </div>
  <div class="person" style="top:180px">
    <span class="person__name">Marisol (Greta) Dovik</span><span class="person__role">Broker</span>
    <div class="license">License No : 0K47382</div>
  </div>
  <div class="contact" style="left:18px;top:250px">
    <div>20387 Marlowpine Dr.</div>
    <div>Tustin, CA 92740</div>
  </div>
  <div class="contact" style="left:190px;top:250px">
    <div class="contact__row"><svg class="icon"><use href="#phone"/></svg>949-555-0147</div>
    <div class="contact__row"><svg class="icon"><use href="#phone"/></svg>949-555-0183</div>
  </div>
  <div class="contact" style="left:345px;top:250px">
    <div class="contact__row"><svg class="icon"><use href="#mail"/></svg>greta@qlbinsurance.example</div>
    <div class="contact__row"><svg class="icon"><use href="#mail"/></svg>qlbinsurance.example</div>
  </div>
</section>

<!-- Back: brand only -->
<section class="card card--back">
  <svg class="card__art" viewBox="0 0 518 307" preserveAspectRatio="none" aria-hidden="true">
    <path d="M0 0H518V20C380 62 170 10 0 40Z" fill="url(#band)"/>
    <path d="M0 58C140 18 330 44 518 22V30C330 56 150 28 0 62Z" fill="#111"/>
    <rect x="0" y="299" width="518" height="4" fill="var(--blue)"/>
  </svg>
  <div class="brand" style="top:104px">
    <div class="brand__mark">QLB</div>
    <div class="brand__name">QLB Insurance Services</div>
    <div class="brand__slogan">Quiet Lanterns Burn</div>
  </div>
</section>

<!-- Front alternative: name in header band -->
<section class="card card--front-b">
  <svg class="card__art" viewBox="0 0 518 307" preserveAspectRatio="none" aria-hidden="true">
    <path d="M0 0H518V62C380 100 170 60 0 86Z" fill="url(#band)"/>
    <path d="M0 104C140 64 330 88 518 70V78C330 100 150 74 0 108Z" fill="#111"/>
    <rect x="0" y="299" width="518" height="4" fill="var(--blue)"/>
  </svg>
  <div class="header-name">
    <div class="header-name__name">Marisol (Greta) Dovik</div>
    <div class="header-name__role">Broker</div>
  </div>
  <div class="brand" style="top:120px">
    <div class="brand__mark">QLB</div>
    <div class="brand__name">QLB Insurance Services</div>
    <div class="brand__slogan">Quiet Lanterns Burn</div>
  </div>
  <div class="contact" style="left:18px;top:237px">
    <div>License No : 0K47382</div>
    <div>20387 Marlowpine Dr.</div>
    <div>Tustin, CA 92740</div>
  </div>
  <div class="contact" style="left:190px;top:252px">
    <div class="contact__row"><svg class="icon"><use href="#phone"/></svg>949-555-0147</div>
    <div class="contact__row"><svg class="icon"><use href="#phone"/></svg>949-555-0183</div>
  </div>
  <div class="contact" style="left:345px;top:252px">
    <div class="contact__row"><svg class="icon"><use href="#mail"/></svg>greta@qlbinsurance.example</div>
    <div class="contact__row"><svg class="icon"><use href="#mail"/></svg>www.qblinsurance.example</div>
  </div>
</section>

<!-- Back alternative: brand with slogan and web -->
<section class="card card--back-b">
  <svg class="card__art" viewBox="0 0 518 307" preserveAspectRatio="none" aria-hidden="true">
    <path d="M0 0H518V20C380 62 170 10 0 40Z" fill="url(#band)"/>
    <path d="M0 58C140 18 330 44 518 22V30C330 56 150 28 0 62Z" fill="#111"/>
    <rect x="0" y="299" width="518" height="4" fill="var(--blue)"/>
  </svg>
  <div class="brand" style="top:100px">
    <div class="brand__mark">QLB</div>
    <div class="brand__name">QLB Insurance Services</div>
    <div class="brand__slogan">Quiet Lanterns Burn</div>
  </div>
  <div class="web">www.qblinsurance.example</div>
</section>

</body>
</html>
```